Logo + Label Design (Men’s Grooming Brand & Product Packaging)

Design a logo and 2 oz pomade label for Rook, a modern men’s grooming brand focused on clean, high-quality, natural ingredients. The design should establish a bold, masculine, minimalist identity that can later extend to products like shaving gel and body wash.

Key Requirements

Create a primary logo for “Rook” and a core label for the 2 oz pomade jar (screw-top).

Use a clean, modern style — masculine, confident, and approachable (think Milton’s, Velta, Northern Guild).

Design for 1–2 color screen printing on solid jar colors (white, black, or navy).

Avoid gradients, foil, or embossing. Must work in black & white.

Provide: vector logo, mockup of the 2 oz jar, color palette (CMYK/RGB/HEX), and font specs.

Winning design may lead to future projects (body wash, shave gel, skincare lines).

Font styles to use
Other font styles liked:
• We like the fonts and design concept in the attached mockup.

Requirements
Should not have
• We want to avoid too much writing or busy designs. We want to avoid having graphics/illustrations embedded in the logo if they will cause the brand to look less classy or sophisticated. We also want the design to look simple and all-American (e.g. Pemberton and Vale, Tall Pine, The LOFT, etc). We’d like to give a Halloway & Brinks vibe that feels classy and high end.

```html
<!DOCTYPE html>
<html lang="en">
<head>
<meta charset="utf-8">
<title>Rook Hair Pomade Label</title>
<link rel="stylesheet" href="https://fonts.googleapis.com/css2?family=Josefin+Sans:wght@400;600;700&display=swap">
<style>
  :root {
    --backdrop: #f2f2f4;
    --jar-black: #060708;
    --ink-white: #ffffff;
  }
  html, body {
    margin: 0;
    padding: 0;
    width: 1200px;
    height: 1000px;
    overflow: hidden;
    background: var(--backdrop);
  }
  .canvas {
    position: relative;
    width: 1200px;
    height: 1000px;
    background: var(--backdrop);
    font-family: "Josefin Sans", "Helvetica Neue", Arial, sans-serif;
    color: var(--ink-white);
  }
  .jar-lid {
    position: absolute;
    left: 277px;
    top: 173px;
    width: 646px;
    height: 646px;
    border-radius: 50%;
    background: var(--jar-black);
  }
  .wordmark {
    position: absolute;
    left: 423px;
    top: 430px;
    width: 356px;
    height: 125px;
    overflow: visible;
  }
  .wordmark text {
    font-family: "Josefin Sans", "Helvetica Neue", Arial, sans-serif;
    font-weight: 700;
    fill: var(--ink-white);
  }
  .product-table {
    position: absolute;
    left: 424px;
    top: 616px;
    width: 355px;
    border-collapse: collapse;
    table-layout: fixed;
  }
  .product-table td {
    border: 1px solid var(--ink-white);
    padding: 0;
    text-align: center;
    vertical-align: middle;
    line-height: 1;
  }
  .col-name { width: 249px; }
  .col-spec { width: 105px; }
  .product-name {
    height: 33px;
    font-size: 24px;
    font-weight: 700;
    letter-spacing: 0.5px;
    padding-top: 4px !important;
  }
  .net-weight {
    font-size: 18px;
    font-weight: 600;
    padding-top: 4px !important;
  }
  .net-weight .unit { font-size: 15px; }
  .net-weight .metric { font-size: 13px; margin-left: 4px; }
  .scent {
    height: 33px;
    font-size: 17px;
    font-weight: 600;
    letter-spacing: 0.6px;
    padding-top: 3px !important;
  }
  .finish-spec {
    font-size: 12px;
    font-weight: 400;
  }
  .finish-spec .spec-line {
    display: block;
    margin: 0 auto;
    width: 82px;
    padding: 2px 0 1px;
  }
  .finish-spec .spec-line + .spec-line {
    border-top: 1px solid var(--ink-white);
  }
</style>
</head>
<body>
  <main class="canvas">
    <div class="jar-lid"></div>

    <svg class="wordmark" viewBox="0 0 356 125" aria-label="Rook">
      <text x="0" y="121" font-size="150" textLength="356" lengthAdjust="spacingAndGlyphs">ROOK</text>
    </svg>

    <table class="product-table">
      <colgroup>
        <col class="col-name">
        <col class="col-spec">
      </colgroup>
      <tr>
        <td class="product-name">HAIR POMADE</td>
        <td class="net-weight">2<span class="unit">OZ</span><span class="metric">(57G)</span></td>
      </tr>
      <tr>
        <td class="scent">FRESH &amp; CLEAN</td>
        <td class="finish-spec">
          <span class="spec-line">medium hold</span>
          <span class="spec-line">matte finish</span>
        </td>
      </tr>
    </table>
  </main>
</body>
</html>
```